Youth basketball program needs a one sided flyer to recruit new players for our competitive teams

We need a flyer to recruit players for our competitive youth basketball teams. Our program is "Lakeshore Ember Basketball" (see www.lsember.example); we are a nonprofit organization that provides opportunities to participate in youth basketball. We are focused on player development (improving each player's fundamentals and related skills.)

We are currently looking for skilled players that will be in the following grades next school year: boys 5th and 6th grade, girls 7th grade. Tryouts will occur in June - July for next season's teams. Girls season goes from October - December (break during January and February so players can play on their school teams) and March - mid April. Boys season goes from November - mid March. Interested players need to contact us to arrange a try out. During the season, teams will practice each week and play in local/regional leagues and tournaments.

We have partnered with Dorian Kessler Basketball Training (see his website at: http://www.dkhoopgrow.example/#!coaching/clinic ) to provide training sessions for all our players.

We would like the following items included in the flyer: our LEB logo, reference to Dorian Kessler and the colors of green & white. The final design should emphasize our focus on player development.

Reason: Designers - thanks for the submissions thus far! I'm currently traveling abroad and haven't been able to provide adequate feedback so I'm going to extend the deadline to allow time for this. Thanks!!

Designers - thank you for all the submissions!  We were very impressed with the creativity and professionalism..  Unfortunately, we can only select one design and we have settled on the flyer/design. Thanks again for your efforts.  - Lakeshore Ember team

Target Market(s)

Boys ages 9-12, girls ages 11-13 and their respective parents.

Industry/Entity Type

Training

Requirements
Must have
• The flyer must include our Lakeshore Ember Basketball logo (can either be the colored logo or the green/white logo), our website address and the Twitter & Facebook logos to direct individuals to our web locations.

```html
<!DOCTYPE html>
<html lang="en">
<head>
<meta charset="utf-8">
<title>Lakeshore Ember Basketball – Tryouts</title>
<link href="https://fonts.googleapis.com/css2?family=Open+Sans:wght@700;800&family=Alegreya:wght@400;700&display=swap" rel="stylesheet">
<style>
  :root {
    --green-deep: #0e2a10;
    --green-mid: #2f4a18;
    --olive: #6b5e22;
    --bronze: #8f6a28;
    --orange: #f26a10;
    --white: #ffffff;
    --badge-navy: #3b5a9a;
    --badge-sky: #5ec8ee;
  }
  * { margin: 0; padding: 0; box-sizing: border-box; }
  html, body { width: 849px; height: 1200px; overflow: hidden; }
  body {
    position: relative;
    background:
      radial-gradient(ellipse 70% 45% at 95% 100%, rgba(160,115,45,.85), transparent 70%),
      linear-gradient(180deg, var(--green-deep) 0%, #143214 35%, var(--green-mid) 58%, var(--olive) 85%, var(--bronze) 100%);
    color: var(--white);
    font-family: "Alegreya", Georgia, serif;
  }
  .flyer-title {
    position: absolute; top: 164px; left: 0; width: 849px;
    text-align: center;
    font-family: "Open Sans", Arial, sans-serif; font-weight: 800; font-size: 45px;
    text-shadow: 2px 2px 3px rgba(0,0,0,.6);
  }
  .flyer-title .accent { color: var(--orange); }
  .intro {
    position: absolute; top: 264px; left: 0; width: 849px;
    text-align: center; font-size: 28px; line-height: 26px;
  }
  .grades {
    position: absolute; top: 322px; left: 0; width: 849px;
    text-align: center; font-size: 26px; font-weight: 700;
  }
  .divider {
    position: absolute; top: 375px; left: 180px; width: 498px; height: 2px;
    background: var(--orange);
  }
  .season {
    position: absolute; top: 389px; left: 210px; width: 437px;
    font-size: 28px; line-height: 25.7px; text-align: justify;
    text-align-last: center;
  }
  .practice {
    position: absolute; top: 567px; left: 0; width: 849px;
    text-align: center; font-size: 25.5px; line-height: 26px;
  }
  .tryout-tag {
    position: absolute; top: 672px; left: 72px; width: 236px; height: 178px;
    background: var(--orange); border-radius: 14px;
    transform: rotate(-8deg);
    box-shadow: 4px 6px 8px rgba(0,0,0,.45);
    display: flex; align-items: center; justify-content: center;
    text-align: center;
    font-family: "Open Sans", Arial, sans-serif; font-weight: 800;
    font-size: 31px; line-height: 30px;
  }
  .contact {
    position: absolute; top: 896px; left: 66px; width: 520px;
    font-size: 28px; line-height: 26px;
  }
  .contact .lead { margin-left: 6px; margin-bottom: 10px; }
  .contact .details { font-size: 27px; line-height: 25.5px; }
  .partners {
    position: absolute; top: 1053px; left: 66px;
    font-size: 17.5px; line-height: 16px;
  }
  .social-row {
    position: absolute; left: 68px;
    display: flex; align-items: center; gap: 10px;
    font-size: 15px;
  }
  .social-row.social-primary { top: 1104px; }
  .social-row.social-secondary { top: 1133px; }
  .social-badge { width: 74px; height: 23px; border-radius: 2px; }
  .social-primary .social-badge { background: var(--badge-navy); border: 2px solid var(--white); }
  .social-secondary .social-badge { background: var(--badge-sky); }
  .program-mark {
    position: absolute; top: 888px; left: 585px; width: 236px;
    text-align: center;
  }
  .program-mark .ball {
    width: 180px; height: 180px; border-radius: 50%;
    background: var(--orange); margin: 0 auto 10px;
  }
  .program-mark .name {
    font-family: "Open Sans", Arial, sans-serif; font-weight: 800; font-size: 22px;
    color: var(--white);
  }
</style>
</head>
<body>
  <h1 class="flyer-title">Lakeshore <span class="accent">EMBER</span> Basketball</h1>

  <p class="intro">We are currently looking for skilled players that<br>will be in the following grades next school year:</p>
  <p class="grades">Boys 5th and 6th grade, Girls 7th grade.</p>
  <div class="divider"></div>

  <p class="season">Girls season goes from October to December (break during January and February so players can play on their school teams) and from March to mid April. Boys season goes from November to mid March.</p>

  <p class="practice">During the season, teams will practice each week<br>and play in local/regional leagues and tournaments.</p>

  <div class="tryout-tag">Tryouts will<br>occur in<br>June/July for<br>next season's<br>teams.</div>

  <div class="contact">
    <p class="lead">Interested players need to<br>contact us to arrange a try out.</p>
    <p class="details">Contact Marcus at 555.014.2290<br>or at team@lsember.example<br>website: http://www.lsember.example/</p>
  </div>

  <p class="partners">Partners: Dorian Kessler Basketball Training<br>http://www.dkhoopgrow.example/#!coaching/clinic</p>

  <div class="social-row social-primary"><span class="social-badge"></span><span>Lakeshore-Ember-Basketball-Inc</span></div>
  <div class="social-row social-secondary"><span class="social-badge"></span><span>@LSEmber</span></div>

  <div class="program-mark">
    <div class="ball"></div>
    <div class="name">Lakeshore Ember</div>
  </div>
</body>
</html>
```